Luxury Lifestyle service requires name card

Logo of my company has to be on the left side of the card. (Blue logo)Name and information preferably on the right side.QR code inclusion would be great , Gold logo if it can be included at the back of the card would be great too- we are a luxury lifestyle concierge company catering to the high net worth clients.

Target Market(s)

high net worth customers / luxury

Industry/Entity Type

Business Service

Contact Information for Business Card

name
contact
email
website

Font styles to use
Serif

Colors
0255a3
3176b5
85abd2
0492cd
33a6d7
85cae6
cee9f5

Requirements
Must have
• Logo of my company has to be on the left side of the card. (Blue logo)
• Name and information on the right side.
Nice to have
• QR code inclusion would be great
Should not have
• Do not use colours :- red , purple , orange , yellow
• background card colour : do not use black

```html
<!DOCTYPE html>
<html lang="en">
<head>
<meta charset="utf-8">
<title>Lumen Daily – Name Card</title>
<link rel="stylesheet" href="https://fonts.googleapis.com/css2?family=Cormorant+Garamond:wght@400;500;600&display=swap">
<style>
  :root {
    --stage: #d6d7d8;
    --stage-light: #eeeeef;
    --card-light: #fbfbfb;
    --card-shade: #e6e6e6;
    --aqua: #64fcef;
    --aqua-edge: #4fd1f2;
    --navy: #0255a3;
    --navy-edge: #3176b5;
    --sky: #85cae6;
    --ink: #3d4244;
  }
  * { margin: 0; padding: 0; box-sizing: border-box; }
  html, body { width: 1200px; height: 1200px; overflow: hidden; }
  body {
    background: radial-gradient(ellipse at 50% 50%, var(--stage-light) 0%, var(--stage) 75%);
    font-family: "Cormorant Garamond", serif;
    color: var(--ink);
    position: relative;
  }
  .card {
    position: absolute;
    left: 166px;
    width: 868px;
    height: 522px;
    overflow: hidden;
    box-shadow: 0 4px 10px rgba(0,0,0,0.25);
  }
  .card--front { top: 56px; }
  .card--back { top: 632px; }
  .card__texture {
    position: absolute; inset: 0;
    background:
      linear-gradient(135deg, var(--card-light) 0%, var(--card-shade) 30%, var(--card-light) 55%, var(--card-shade) 80%, var(--card-light) 100%);
  }
  .card__wings { position: absolute; inset: 0; }
  .brand {
    position: absolute;
    display: flex;
    flex-direction: column;
    align-items: center;
    transform: translateX(-50%);
  }
  .brand__dot { border-radius: 50%; }
  .brand__name {
    font-weight: 500;
    color: var(--ink);
    white-space: nowrap;
    line-height: 1;
  }
  .card--front .brand { left: 294px; top: 155px; }
  .card--front .brand__dot { width: 146px; height: 146px; background: var(--aqua); }
  .card--front .brand__name { font-size: 42px; letter-spacing: 1px; margin-top: 38px; }
  .card--back .brand { left: 434px; top: 87px; }
  .card--back .brand__dot { width: 230px; height: 230px; background: var(--navy-edge); }
  .card--back .brand__name { font-size: 64px; letter-spacing: 2px; margin-top: 60px; }
  .contact {
    position: absolute;
    left: 466px;
    top: 178px;
  }
  .contact__name { font-size: 44px; font-weight: 500; line-height: 1; margin-bottom: 14px; }
  .contact__line { font-size: 21px; font-weight: 600; line-height: 26px; }
</style>
</head>
<body>
  <section class="card card--front">
    <div class="card__texture" role="img" aria-label="Soft white quilted diamond pattern"></div>
    <svg class="card__wings" viewBox="0 0 868 522" aria-hidden="true">
      <path d="M0,0 Q40,175 162,261 Q40,347 0,522 Z" fill="var(--aqua-edge)"/>
      <path d="M0,10 Q32,180 146,261 Q32,342 0,512 Z" fill="var(--aqua)"/>
      <path d="M868,0 Q828,175 706,261 Q828,347 868,522 Z" fill="var(--aqua-edge)"/>
      <path d="M868,10 Q836,180 722,261 Q836,342 868,512 Z" fill="var(--aqua)"/>
    </svg>
    <div class="brand">
      <div class="brand__dot"></div>
      <div class="brand__name">LUMEN DAILY</div>
    </div>
    <div class="contact">
      <h1 class="contact__name">Clara Wen</h1>
      <p class="contact__line">12 Marlow Crescent</p>
      <p class="contact__line">Singapore 408812</p>
      <p class="contact__line">hello@lumendaily.com</p>
      <p class="contact__line">+65310004726</p>
      <p class="contact__line">www.lumendaily.com</p>
    </div>
  </section>

  <section class="card card--back">
    <div class="card__texture" role="img" aria-label="Soft white quilted diamond pattern"></div>
    <svg class="card__wings" viewBox="0 0 868 522" aria-hidden="true">
      <path d="M0,0 Q40,175 162,261 Q40,347 0,522 Z" fill="var(--sky)"/>
      <path d="M0,10 Q32,180 146,261 Q32,342 0,512 Z" fill="var(--navy)"/>
      <path d="M868,0 Q828,175 706,261 Q828,347 868,522 Z" fill="var(--sky)"/>
      <path d="M868,10 Q836,180 722,261 Q836,342 868,512 Z" fill="var(--navy)"/>
    </svg>
    <div class="brand">
      <div class="brand__dot"></div>
      <div class="brand__name">LUMEN DAILY</div>
    </div>
  </section>
</body>
</html>
```